Business Card Design Project

Personal Service. There are three areas of my service: Resourceful/Recycling Consultation, Life Coaching using Law of Attraction & Visualization Board. My current cards has: Envision to Becoming. I would like to work with this theme

Industry/Entity Type

Business

Contact Information for Business Card

Circles. Recyling Triangle

```html
<!DOCTYPE html>
<html lang="en">
<head>
<meta charset="utf-8">
<title>Envision to Becoming – Business Cards</title>
<link rel="stylesheet" href="https://fonts.googleapis.com/css2?family=Cinzel:wght@700&family=Open+Sans:wght@400&display=swap">
<style>
  :root {
    --magenta: #b8086e;
    --green: #7dbe3a;
    --white: #ffffff;
    --backdrop: #ebe7e3;
    --serif: "Cinzel", serif;
    --sans: "Open Sans", Arial, sans-serif;
  }
  * { margin: 0; padding: 0; box-sizing: border-box; }
  html, body { width: 1200px; height: 900px; overflow: hidden; }
  body { position: relative; background: var(--backdrop); font-family: var(--sans); }

  .card { position: absolute; background: var(--white); overflow: hidden; box-shadow: 0 6px 18px rgba(0,0,0,.18); }
  .card-front { left: 78px; top: 35px; width: 587px; height: 362px; }
  .card-back { left: 388px; top: 505px; width: 567px; height: 352px; }

  .card-bands { position: absolute; inset: 0; }

  .brand-name {
    position: absolute; left: 0; right: 0; text-align: center;
    font-family: var(--sans); font-weight: 400; color: var(--magenta);
    line-height: 1.15;
  }
  .card-front .brand-name { top: 66px; font-size: 40px; }

  .contact-list { position: absolute; left: 30px; top: 272px; list-style: none; color: var(--white); font-size: 15px; line-height: 21px; }
  .contact-list li { display: flex; align-items: center; gap: 8px; }
  .contact-list svg { width: 12px; height: 12px; fill: var(--white); }

  .holder { position: absolute; right: 36px; top: 242px; text-align: right; color: var(--white); }
  .holder-name { font-family: var(--serif); font-weight: 700; font-size: 18px; line-height: 22px; letter-spacing: .5px; }
  .holder-role { font-size: 15px; line-height: 20px; margin-top: 0; }
  .holder-address { font-size: 15px; line-height: 22px; margin-top: 8px; }

  .brand-dot { position: absolute; left: 258px; top: 72px; width: 52px; height: 52px; border-radius: 50%; background: var(--magenta); }
  .card-back .brand-name { top: 158px; font-size: 30px; }

  .services { position: absolute; left: 0; bottom: 0; width: 100%; height: 84px; background: var(--magenta); color: var(--white); text-align: center; font-size: 15px; line-height: 21px; padding-top: 14px; }
</style>
</head>
<body>

<section class="card card-front" aria-label="Card front">
  <svg class="card-bands" viewBox="0 0 587 362" aria-hidden="true">
    <polygon points="0,198 384,198 362,224 0,224" fill="var(--green)"/>
    <polygon points="0,228 365,228 392,190 587,190 587,362 0,362" fill="var(--magenta)"/>
  </svg>

  <h1 class="brand-name">Envision to<br>Becoming</h1>

  <ul class="contact-list">
    <li><svg viewBox="0 0 12 12"><path d="M3 0h6a1 1 0 0 1 1 1v10a1 1 0 0 1-1 1H3a1 1 0 0 1-1-1V1a1 1 0 0 1 1-1zm0 1.5v7.5h6V1.5z"/></svg>044-555 010 234</li>
    <li><svg viewBox="0 0 12 12"><path d="M0 3c2-2 10-2 12 0v2H9V3.5H3V5H0zM2 6h8l1.5 5h-11zm4 1.2a1.6 1.6 0 1 0 0 3.2a1.6 1.6 0 0 0 0-3.2z"/></svg>044-555 010 234</li>
    <li><svg viewBox="0 0 12 12"><path d="M0 2h12v1L6 7 0 3zm0 2.5 6 4 6-4V10H0z"/></svg>hello@envisionbecoming.com</li>
  </ul>

  <div class="holder">
    <p class="holder-name">Daniel Hart</p>
    <p class="holder-role">Managing Director</p>
    <p class="holder-address">12345, Address Goes Here<br>Country Name, 123456</p>
  </div>
</section>

<section class="card card-back" aria-label="Card back">
  <span class="brand-dot" aria-hidden="true"></span>
  <h2 class="brand-name">Envision to<br>Becoming</h2>
  <p class="services">Resourceful/Recycling Consultation<br>Life Coaching using Law of Attraction | Visualization Board</p>
</section>

</body>
</html>
```